Corporate flyer highlighting service offering for PR agency

A corporate flyer is needed for a new service offering that we are doing. The product name is HarborLeap it is a marketing and communications services offering for companies who are getting ready to sell their business. If we are really happy with the designer's work, there will be a great deal more projects. I am looking for a clean design with a few pops of color from my site. https://quillmarsh.partners. I am looking for a good design with data in sections. I am looking for a clean design that feels high-end but not cluttered. Please do not use images of people. Please see the following examples of types of designs I like.
https://www.tackboard.example/pin/839201746530918264/
https://www.tackboard.example/pin/402918375561029847/
https://assets.stockvale.example/corporate-flyer-template-KRTPMB
https://designbrook.example/item/corporate-flyer-template/81046395?s_rank=8
https://assets.stockvale.example/corporate-business-flyer-template-93PX7D

I had to place the project on hold as I choose the wrong type of project and did not get many designs as a result. I am reposting this with an updated brief.

Target Market(s)

Business sellers and brokers

Industry/Entity Type

Marketing for business sellers

Font styles to use
Sans Serif

Requirements
Must have
• Good quality design with content in sections. Clean and high end feeling is a must.
Should not have
• A lot of images of people.

```html
<!DOCTYPE html>
<html lang="en">
<head>
<meta charset="utf-8">
<title>HarborLeap Service Flyer</title>
<link href="https://fonts.googleapis.com/css2?family=Open+Sans:wght@300;400;600;700&family=Roboto+Condensed:wght@700&family=Raleway:wght@300;400&display=swap" rel="stylesheet">
<style>
:root{
  --stage:#636363;
  --paper:#ffffff;
  --blue:#2b96d9;
  --blue-deep:#0b6db5;
  --blue-light:#3fa9e6;
  --orange:#f39200;
  --ember:#e6501b;
  --green:#6aa935;
  --green-dark:#3f7f1d;
  --ink:#333333;
  --mist:#e4e9ee;
}
*{margin:0;padding:0;box-sizing:border-box}
html,body{width:1200px;height:2984px;overflow:hidden;background:var(--stage)}
body{position:relative;font-family:"Open Sans",Arial,sans-serif;color:var(--ink)}
.defs{position:absolute;width:0;height:0}
.page{position:absolute;width:476px;height:674px;background:var(--paper);overflow:hidden}
.page > *{position:absolute}
.col-l{left:95px}.col-r{left:629px}
.row1{top:81px}.row2{top:799px}.row3{top:1517px}.row4{top:2235px}
.motif{display:block}
.brand{left:30px;top:58px;font-size:17px;font-weight:700;color:var(--ink);letter-spacing:.5px;display:flex;align-items:center;gap:8px}
.brand .mark{width:12px;height:12px;background:var(--orange)}
.hero-title{left:28px;top:296px;font-family:"Raleway",sans-serif;font-weight:300;font-size:35px;color:var(--green)}
.hero-sub{left:29px;top:340px;width:230px;font-family:"Raleway",sans-serif;font-size:19px;line-height:25px}
.hero-sub .b{color:var(--blue)}.hero-sub .o{color:var(--ember)}
.small{font-size:7.6px;line-height:10.5px;color:#444}
.contact{left:218px;font-family:"Raleway",sans-serif;font-size:15px;color:var(--ink)}
.contact i{display:inline-block;width:9px;height:7px;background:var(--blue);margin-right:7px;vertical-align:1px}
.quote-band{left:0;width:476px;background:var(--blue);color:#fff}
.qm{color:var(--orange);font-family:Georgia,serif;font-weight:700;font-size:30px;line-height:1;position:absolute}
.lead{font-size:13.4px;line-height:17.5px;font-weight:700;color:var(--blue-deep)}
.body{font-size:11.2px;line-height:15px;color:var(--ink)}
.chips{left:28px;top:391px;display:flex;gap:5px}
.chip{background:var(--orange);color:#fff;font-size:10px;font-weight:600;height:48px;display:flex;align-items:center;padding:0 7px;line-height:14px}
.label{background:var(--green);color:#fff;font-weight:700;font-size:12.5px;height:26px;display:flex;align-items:center;padding:0 19px}
.txt{font-size:9.5px;line-height:13px;color:#444}
.icons{left:30px;top:394px;display:flex}
.icon-col{width:110px;text-align:center;border-left:1px solid #d7b98a}
.icon-col:first-child{border-left:none}
.icon-col svg{width:74px;height:68px;display:block;margin:0 auto}
.icon-col p{font-size:7.6px;line-height:10px;margin-top:10px;color:#444}
.bullets{list-style:none}
.bullets li{position:relative;padding-left:24px;margin-bottom:10px}
.bullets li::before{content:"";position:absolute;left:0;top:3px;width:0;height:0;border-left:6px solid var(--blue);border-top:5px solid transparent;border-bottom:5px solid transparent}
.bullets li::after{content:"";position:absolute;left:6px;top:3px;width:0;height:0;border-right:5px solid var(--orange);border-top:5px solid transparent;border-bottom:5px solid transparent;transform:scaleX(-1)}
.cite{font-family:"Roboto Condensed",sans-serif;font-weight:700;font-size:12.5px;color:var(--green-dark)}
.stat{font-size:13.6px;line-height:18px;color:var(--ink)}
.sec-title{font-weight:700;font-size:13px;line-height:17px;color:var(--ember)}
.rule-orange{height:4px;background:var(--orange)}
.rule-blue{height:4px;background:var(--blue-deep)}
.rule-green{height:4px;background:var(--green)}
.hat{font-size:16px;font-weight:700;color:var(--green-dark)}
.fine{font-size:7.6px;line-height:10.5px;color:#444}
</style>
</head>
<body>

<svg class="defs" aria-hidden="true">
  <defs>
    <linearGradient id="tone-blue" x1="0" y1="0" x2="1" y2="1"><stop offset="0" stop-color="#3fa9e6"/><stop offset="1" stop-color="#0b6db5"/></linearGradient>
    <linearGradient id="tone-mix" x1="0" y1="0" x2="1" y2="1"><stop offset="0" stop-color="#2b96d9"/><stop offset=".55" stop-color="#3fa9e6"/><stop offset=".8" stop-color="#f39200"/><stop offset="1" stop-color="#0b6db5"/></linearGradient>
    <linearGradient id="tone-warm" x1="0" y1="0" x2="1" y2="0"><stop offset="0" stop-color="#e6501b"/><stop offset=".45" stop-color="#f39200"/><stop offset="1" stop-color="#2b96d9"/></linearGradient>
    <linearGradient id="tone-warm-r" x1="0" y1="0" x2="1" y2="0"><stop offset="0" stop-color="#2b96d9"/><stop offset=".55" stop-color="#f39200"/><stop offset="1" stop-color="#e6501b"/></linearGradient>
    <linearGradient id="tone-laptop" x1="0" y1="0" x2="1" y2="1"><stop offset="0" stop-color="#eef1f4"/><stop offset=".5" stop-color="#9aa6b1"/><stop offset="1" stop-color="#3a4651"/></linearGradient>
    <linearGradient id="tone-city" x1="0" y1="0" x2="0" y2="1"><stop offset="0" stop-color="#b7ddf3"/><stop offset=".5" stop-color="#4f9fd4"/><stop offset="1" stop-color="#173f66"/></linearGradient>
    <linearGradient id="tone-desk" x1="0" y1="0" x2="0" y2="1"><stop offset="0" stop-color="#2e5f8e"/><stop offset=".6" stop-color="#8fb4d3"/><stop offset="1" stop-color="#e8eef4"/></linearGradient>
  </defs>
</svg>

<!-- Page 1: cover -->
<section class="page col-l row1">
  <svg class="motif" role="img" aria-label="Geometric blue and orange triangle motif" style="left:0;top:0;width:476px;height:674px" viewBox="0 0 476 674">
    <polygon points="0,150 200,150 85,285" fill="var(--mist)"/>
    <polygon points="225,0 476,0 476,310 400,330 300,210 225,120" fill="url(#tone-mix)"/>
    <polygon points="110,245 160,140 210,140 195,245" fill="url(#tone-warm)"/>
    <polygon points="0,560 0,674 180,674 195,620 60,620" fill="url(#tone-warm)"/>
  </svg>
  <svg role="img" aria-label="Laptop showing analytics charts with a hand taking notes" style="left:160px;top:170px;width:222px;height:136px" viewBox="0 0 222 136">
    <polygon points="55,0 222,0 222,136 0,136" fill="url(#tone-laptop)"/>
  </svg>
  <svg role="img" aria-label="Blue-toned city skyline with business travellers walking" style="left:300px;top:300px;width:176px;height:280px" viewBox="0 0 176 280">
    <polygon points="20,0 176,0 176,70 112,280 0,110" fill="url(#tone-city)"/>
  </svg>
  <div class="brand"><span class="mark"></span>QUILLMARSH PARTNERS</div>
  <h1 class="hero-title">HarborLeap</h1>
  <p class="hero-sub"><span class="b">provides executives and business owners with</span> <span class="o">clear guidance to unlock non-financial value ahead of an exit.</span></p>
  <p class="small" style="left:30px;top:480px;width:290px">A strong communication and marketing strategy can significantly increase the value of your business leading up to an exit. Buyers are looking to mitigate risk and unlock potential value as a catalyst for clear growth potential.</p>
  <p class="small" style="left:30px;top:526px;width:330px">Highlighting your company's success in the marketplace, identifying, and mitigating reputation risks before buyers do, enhancing employee engagement, finding hidden opportunities to boost marketing KPIs and showcasing IP, data, and innovation, can make a significant difference in valuation.</p>
  <p class="contact" style="top:612px"><i></i>info@quillmarsh.partners</p>
  <p class="contact" style="top:636px"><i style="border-radius:50%;width:8px;height:8px"></i>www.quillmarsh.partners</p>
</section>

<!-- Page 2 -->
<section class="page col-r row1">
  <svg class="motif" role="img" aria-label="Geometric blue and orange triangle motif" style="left:285px;top:545px;width:191px;height:129px" viewBox="0 0 191 129">
    <polygon points="0,70 130,70 191,0 191,129 30,129" fill="url(#tone-warm-r)"/>
  </svg>
  <div class="quote-band" style="top:25px;height:172px">
    <span class="qm" style="left:26px;top:26px">“</span>
    <p style="position:absolute;left:52px;top:38px;width:395px;font-size:13.6px;line-height:19.5px;font-weight:300">US institutional investors believe that Investor Relations (IR) accounts for a total variance of 30% in a company's valuation – from a premium of 10% for “superb” IR to a discount of 20% for “poor” IR.&nbsp; ---Corvane Research Group, “Harnessing IR's Power to Impact a Company's Valuation.</p>
    <span class="qm" style="left:436px;top:134px">”</span>
  </div>
  <p class="lead" style="left:30px;top:246px;width:405px;font-size:13px">We design and implement communication and marketing strategies that deliver significant increases in brand awareness, identify reputational risks, and enhance brand perception, helping owners and investors to realize premium values for their companies. We support owners and companies through:</p>
  <div class="chips">
    <span class="chip" style="width:89px">Company Exit Preparation</span>
    <span class="chip" style="width:54px;justify-content:center">M&amp;A</span>
    <span class="chip" style="width:56px;justify-content:center">IPO</span>
    <span class="chip" style="width:90px;padding-left:14px">Spinoff/ Divestiture</span>
    <span class="chip" style="width:104px">New Leadership/ Investor</span>
  </div>
  <p class="body" style="left:30px;top:478px;width:416px">Few sellers would list their home without first inspecting, repairing broken items, and making updates to highlight the positive aspects --increasing appeal to buyers. However, countless business owners leave money on the table during corporate exits due to a lack of preparation.</p>
</section>

<!-- Page 3 -->
<section class="page col-l row2">
  <svg class="motif" role="img" aria-label="Geometric blue triangle motif" style="left:270px;top:0;width:206px;height:245px" viewBox="0 0 206 245">
    <polygon points="0,0 206,0 206,245 100,245 70,130 130,120" fill="url(#tone-blue)"/>
  </svg>
  <svg class="motif" role="img" aria-label="Geometric blue triangle motif" style="left:0;top:585px;width:130px;height:89px" viewBox="0 0 130 89">
    <polygon points="0,0 60,0 80,40 130,89 0,89" fill="url(#tone-blue)"/>
  </svg>
  <p class="txt" style="left:30px;top:78px;width:270px">Our team of executive-level communications and marketing experts brings deep buy and sell-side experience. We have played critical roles in the acquisition, integration, and disposition process. Our mix of financial services expertise combined with decades of experience leading internal and external communications, marketing and investor relations teams gives us a unique perspective on identifying and unlocking non-financial areas of value and mitigating non-financial risks before exit.</p>
  <p class="txt" style="left:30px;top:226px;width:345px">While accounting and investment banking teams are hard at work increasing value from a financial perspective, we help organizations enhance their valuation by identifying areas that will appeal most to buyers and ensuring those elements of your business are visible and memorable to those who matter most.</p>
  <div class="label" style="left:30px;top:341px;width:356px">WE HELP COMPANIES INCREASE VALUATION BY:</div>
  <div class="icons">
    <div class="icon-col">
      <svg viewBox="0 0 74 68"><polygon points="19,2 55,2 73,34 55,66 19,66 1,34" fill="var(--orange)" stroke="var(--ember)" stroke-width="3"/><polygon points="37,14 24,30 32,30 32,50 42,50 42,30 50,30" fill="#fff"/><circle cx="49" cy="48" r="7" fill="#fff"/><polyline points="45,48 48,51 53,45" fill="none" stroke="var(--orange)" stroke-width="2"/></svg>
      <p>Highlighting value<br>in a clear<br>and visible way</p>
    </div>
    <div class="icon-col">
      <svg viewBox="0 0 74 68"><polygon points="19,2 55,2 73,34 55,66 19,66 1,34" fill="var(--orange)" stroke="var(--ember)" stroke-width="3"/><circle cx="42" cy="28" r="11" fill="none" stroke="#fff" stroke-width="4"/><line x1="34" y1="36" x2="22" y2="48" stroke="#fff" stroke-width="5"/><polygon points="45,40 53,52 37,52" fill="#fff"/></svg>
      <p>Identifying potential<br>risks and suggesting<br>mitigation measures</p>
    </div>
    <div class="icon-col">
      <svg viewBox="0 0 74 68"><polygon points="19,2 55,2 73,34 55,66 19,66 1,34" fill="var(--orange)" stroke="var(--ember)" stroke-width="3"/><circle cx="37" cy="34" r="15" fill="none" stroke="#fff" stroke-width="4" stroke-dasharray="20 4"/><circle cx="37" cy="34" r="6" fill="#fff"/></svg>
      <p>Streamlining<br>the exit process</p>
    </div>
    <div class="icon-col">
      <svg viewBox="0 0 74 68"><polygon points="19,2 55,2 73,34 55,66 19,66 1,34" fill="var(--orange)" stroke="var(--ember)" stroke-width="3"/><rect x="28" y="16" width="20" height="28" fill="none" stroke="#fff" stroke-width="2"/><rect x="24" y="20" width="20" height="28" fill="#fff"/><line x1="28" y1="28" x2="40" y2="28" stroke="var(--orange)" stroke-width="2"/><line x1="28" y1="34" x2="40" y2="34" stroke="var(--orange)" stroke-width="2"/><line x1="28" y1="40" x2="40" y2="40" stroke="var(--orange)" stroke-width="2"/></svg>
      <p>Creating a polished<br>presence in the market<br>ahead of buyer interest</p>
    </div>
  </div>
</section>

<!-- Page 4 -->
<section class="page col-r row2">
  <svg class="motif" role="img" aria-label="Geometric blue and orange triangle motif" style="left:15px;top:630px;width:100px;height:44px" viewBox="0 0 100 44">
    <polygon points="0,44 25,0 75,0 70,20 100,44" fill="url(#tone-warm-r)"/>
  </svg>
  <div class="rule-blue" style="left:112px;top:654px;width:364px"></div>
  <p class="lead" style="left:29px;top:56px;width:400px">HarborLeap provides executives and business owners with clear guidance to unlock value ahead of an exit. Our non-disruptive, ala-carte process enables us to work with sellers on specific areas or to do a complete analysis and recommendation and can include:</p>
  <div class="label" style="left:29px;top:194px;width:312px">BRAND ANALYSIS AND RECOMMENDATIONS</div>
  <p class="txt" style="left:29px;top:229px;width:340px">Strong brands command a higher valuation. We conduct a brand analysis, providing clear and detailed recommendations to enhance your value proposition and help you stand out from the crowd:</p>
  <ul class="bullets txt" style="left:29px;top:292px;width:420px">
    <li style="margin-bottom:26px">Current external position among competitors --We look at how your brand measures up based on external competitive analysis, positioning in the media and analyst community, and across other digital channels.</li>
    <li style="margin-bottom:26px">Physical brand image--A little bit of paint and updated fixtures can go a long way when increasing the value of a home. The same is true for businesses. Our audit evaluates non-disruptive steps your company can take to enhance your brand look and feel before sale.</li>
    <li style="margin-bottom:26px">Employee brand perception--We conduct a high-level external audit with recommendations to enhance engagement for current and prospective employees.</li>
    <li>Customer brand perception-- We conduct a high-level external audit showcasing how customers perceive your brand in the market. We then provide recommendations for enhancing engagement and maximizing value.</li>
  </ul>
</section>

<!-- Page 5 -->
<section class="page col-l row3">
  <p class="stat" style="left:29px;top:82px;width:420px">A 5% increase in customer retention correlates with at least a 25% increase in profit, according to an analysis by Halden &amp; Company.</p>
  <p class="cite" style="left:29px;top:126px;font-family:'Open Sans',sans-serif;font-size:11.5px">(https://files.haldenco.example/briefs/retention_costs.pdf)</p>
  <p class="stat" style="left:29px;top:179px;width:420px">It costs 5 times more to acquire a new customer than to retain a current one and 16 times more to get new customers to the same spending level as existing ones.</p>
  <p class="cite" style="left:29px;top:254px">(https://growthledger.example/customer-retention-guide-statistics/)</p>
  <div class="rule-orange" style="left:29px;top:318px;width:225px"></div>
  <p class="sec-title" style="left:27px;top:386px;width:400px">DIGITAL AND TRADITIONAL MARKETING ANALYSIS AND RECOMMENDATIONS</p>
  <p class="txt" style="left:27px;top:428px;width:400px">How much money are you leaving on the table? Our marketing audits help organizations identify areas of hidden value that can have significant impacts on revenue and valuation. We optimize current activities and uncover new strategies to increase the effectiveness of current marketing spend. Areas we evaluate include:</p>
  <ul class="bullets" style="left:27px;top:520px;width:190px;font-size:11px;line-height:14.5px">
    <li style="margin-bottom:4px">Website traffic and conversion</li>
    <li style="margin-bottom:4px">CRM process review to identify strategies and recommendations to increase conversion and reactive old-leads</li>
    <li>Email marketing strategy</li>
  </ul>
  <div style="left:234px;top:520px;width:1px;height:95px;background:#d7b98a"></div>
  <ul class="bullets" style="left:267px;top:520px;width:200px;font-size:11px;line-height:14.5px">
    <li style="margin-bottom:6px">Automations and drip marketing</li>
    <li style="margin-bottom:6px">Social media strategy /presence</li>
    <li style="margin-bottom:6px">Partnership marketing</li>
    <li>Paid media analysis/strategy suggestion</li>
  </ul>
</section>

<!-- Page 6 -->
<section class="page col-r row3">
  <svg class="motif" role="img" aria-label="Geometric blue triangle motif" style="left:270px;top:0;width:206px;height:205px" viewBox="0 0 206 205">
    <polygon points="0,0 206,0 206,205 170,205 70,115 60,50" fill="url(#tone-blue)"/>
  </svg>
  <svg class="motif" role="img" aria-label="Geometric blue and orange triangle motif" style="left:15px;top:630px;width:100px;height:44px" viewBox="0 0 100 44">
    <polygon points="0,44 25,0 75,0 70,20 100,44" fill="url(#tone-warm-r)"/>
  </svg>
  <svg role="img" aria-label="Business analyst reviewing financial charts on a tablet" style="left:38px;top:8px;width:282px;height:222px" viewBox="0 0 282 222">
    <polygon points="190,0 282,222 0,222" fill="url(#tone-desk)"/>
  </svg>
  <div class="rule-blue" style="left:112px;top:654px;width:364px"></div>
  <p class="sec-title" style="left:28px;top:299px;font-size:12.8px">MESSAGING AND CONTENT&nbsp; STRATEGY REVIEW AND ANALYSIS</p>
  <p class="lead" style="left:28px;top:326px;width:425px;font-size:11.4px;line-height:15px">It's about your valuation. Full and fair valuation requires a clear, compelling investment case articulated consistently to the right audience at the right time. Messaging to maximize your value in an acquisition or an IPO is quite different from typical selling messages for prospects, customers, or 'features &amp; business benefits' for press and analysts.&nbsp; We understand the issues and speak the right language to maximize perception of value with key decision makers.</p>
  <ul class="bullets txt" style="left:28px;top:466px;width:200px">
    <li style="margin-bottom:14px">Review and recommendations of key messaging and value proposition</li>
    <li>Analysis and recommendations to position key executives likely to remain with the company as thought leaders to help build value</li>
  </ul>
  <ul class="bullets txt" style="left:245px;top:466px;width:200px">
    <li style="margin-bottom:14px">Analysis and recommendations to highlight data, IP, and innovation</li>
    <li>Analysis and recommendations to build employee engagement and retention enhancing your most valuable asset--your team</li>
  </ul>
</section>

<!-- Page 7 -->
<section class="page col-l row4">
  <div style="left:0;top:378px;width:476px;height:6px;background:#eeeeee"></div>
  <svg class="motif" role="img" aria-label="Geometric blue and orange triangle motif" style="left:355px;top:384px;width:121px;height:121px" viewBox="0 0 121 121">
    <polygon points="0,0 121,0 121,85 57,121" fill="url(#tone-warm-r)"/>
  </svg>
  <svg class="motif" role="img" aria-label="Geometric blue and orange triangle motif" style="left:380px;top:600px;width:96px;height:74px" viewBox="0 0 96 74">
    <polygon points="0,74 20,30 60,30 96,0 96,74" fill="url(#tone-warm-r)"/>
  </svg>
  <div class="rule-green" style="left:0;top:658px;width:380px"></div>
  <div class="label" style="left:30px;top:61px;width:334px;font-size:12px">MEDIA AND ANALYST STRATEGY DEVELOPMENT</div>
  <p class="txt" style="left:30px;top:113px;width:415px;font-size:10.4px;line-height:15px">Positive articles and inclusion in analyst reports pack a powerful punch when preparing your business for sale. We work with clients to develop a media strategy that goes beyond brand awareness, leveraging media to build a digital history of third-party validation targeted to enhance appeal to prospective buyers while generating traffic and connections, to enhance overall value.</p>
  <ul class="bullets txt" style="left:30px;top:228px;width:380px;font-size:10.4px;line-height:14px">
    <li style="margin-bottom:6px">Positioning to media and analyst community creating third party market validation</li>
    <li style="margin-bottom:6px">Key angle recommendations</li>
    <li style="margin-bottom:10px">Announcement timeline and strategy planning to maximize media value of news</li>
    <li style="margin-left:22px;margin-bottom:12px">What is newsworthy</li>
    <li style="margin-left:22px">How to position that news for the most significant impact</li>
  </ul>
  <span class="qm" style="left:28px;top:452px;font-size:28px">“</span>
  <p class="hat" style="left:54px;top:462px">WHITE HAT/BLACK HAT REVIEW</p>
  <span class="qm" style="left:314px;top:452px;font-size:28px">”</span>
  <p class="txt" style="left:30px;top:500px;width:375px;font-size:10.4px;line-height:15px">We take a buyer's communications and marketing approach to analyzing the client company and provide a “punch list” of things a potential buyer is likely to ask/request in due diligence from a comms/culture/marketing/reputation standpoint to ensure that when potential buyers start screening for sellers and evaluating them, the client company has the upper hand.</p>
</section>

<!-- Page 8 -->
<section class="page col-r row4">
  <svg class="motif" role="img" aria-label="Geometric blue and orange triangle motif" style="left:255px;top:530px;width:221px;height:144px" viewBox="0 0 221 144">
    <polygon points="0,80 135,90 221,0 221,144 45,144" fill="url(#tone-warm-r)"/>
  </svg>
  <div class="quote-band" style="top:27px;height:106px">
    <span class="qm" style="left:26px;top:24px">“</span>
    <p style="position:absolute;left:50px;top:34px;width:390px;font-size:14.4px;line-height:19.5px;font-weight:700">Strategy without tactics is the slowest route to victory. Tactics without strategy is the noise before defeat.</p>
    <span class="qm" style="left:108px;top:75px">”</span>
  </div>
  <p style="left:29px;top:156px;width:420px;font-size:11px;line-height:14.5px;color:var(--blue)">Once the analysis is complete, we deliver actionable intelligence and recommendations to help leaders identify and quickly unlock areas that will boost value and appeal to prospective buyers. Work products include:</p>
  <ul class="bullets txt" style="left:29px;top:228px;width:420px;font-size:9.2px;line-height:12.5px">
    <li style="padding-left:40px;margin-bottom:12px">Gap Assessment -- We provide a comprehensive seller report providing analysis and actionable recommendations to increase your valuation while identifying and mitigating non-financial risks.</li>
    <li style="padding-left:40px">Strategic Roadmap -- Clients are given an actionable tactical roadmap based on the recommendation provided. Organizations can choose to implement key areas or include this powerful guide as part of their presentation to prospective buyers to highlight latent potential. The roadmap provides actionable steps buyers can take upon close as they make their case for your business with their investment committees.</li>
  </ul>
  <p class="fine" style="left:29px;top:406px;width:420px">Once the strategy integration roadmap is complete, your team can implement it on your timeline, we can work with your team providing guidance and executive-level support, or we can fully execute deliverables with our robust capabilities and team.</p>
  <p class="fine" style="left:29px;top:454px;width:420px">Our value proposition, based on delivering outcomes rather than just outputs, means that you receive the benefit and capability of deeply experienced corporate communications leaders without adding headcount or the time to identify, recruit, onboard and retain a new team member.</p>
  <p class="fine" style="left:29px;top:503px;width:420px">We help organizations enhance their valuation by identifying areas that will appeal most to buyers and ensuring those elements of your business are visible and memorable to those who matter most.</p>
  <p class="fine" style="left:29px;top:540px;width:300px">HarborLeap helps sellers maximize valuation and unlock hidden potential ahead of an exit--ensuring money is not left on the table.</p>
</section>

</body>
</html>
```